Label for Dog Nourishing CBD Balm

Dear Designers,

We are looking for a packaging expert to design our new Hydrating Balm for dogs which contain a relaxing hemp extract (CBD). The product is intended to be massaged on the dog’s paws to make them softer and promote the animal’s well-being :)

Our company is already selling various relaxing cat & dog products, and we would like this new design to reflect the same "style & feeling" as our current products (see attached ZIP file).

Technical aspects:
- The packaging is a 40ml aluminium jar (58mm x 23mm).
- We are looking to design 2 separate labels (one for the front, one for the back)
- The label dimensions should be : 50mm x 50mm
- Please follow technical guidelines from printer (see ZIP file).

Design aspects:
- The design should be compatible with our brand identity (i.e. fluffly, pure, relaxing, positive, clean & natural).
- People should understand what the product "is" and what the product "does" simply from looking at the design.
- The actual balm is white/yellow in color.
- Soft/rounded shapes are preferred.
- Please use our brand's colors (see typo & colors in ZIP file)
- Please use our brand's fonts (see typo & colors in ZIP file)
- Please use our company logo (see ZIP file).
- The design also needs to convey a strong sense of professionalism as we are an animal "healthcare" brand.
- If you want to include a dog picture, we would prefer you to use a picture of our official brand ambassador (see ZIP file).
- Only original work (no plagiarism will be accepted).

Please don't hesitate to send us a message if you have any questions about the brand, the product or the design requirements.

We look forward to seeing your designs & working on this together !

Thanks & regards,
Marcus

Target Market(s)

Dog owners

Font styles to use
Other font styles liked:
• See ZIP file

Requirements
Must have
• Brand fonts (see typo & colors in ZIP file)
Brand colors (see typo & colors in ZIP file)

```html
<!DOCTYPE html>
<html lang="en">
<head>
<meta charset="utf-8">
<title>Verdalis Soothing Balm – Lid Label</title>
<link rel="stylesheet" href="https://fonts.googleapis.com/css2?family=Arvo:wght@400;700&family=Montserrat:wght@500;600&family=Roboto+Condensed:wght@300;400&display=swap">
<style>
  :root {
    --page-bg: #f5f5f5;
    --label-white: #ffffff;
    --brand-green: #3ca585;
    --ink-dark: #1b2e1c;
    --thc-orange: #f07a1e;
    --fur-light: #ecebe6;
    --fur-shade: #c9c4ba;
  }
  * { margin: 0; padding: 0; box-sizing: border-box; }
  html, body {
    width: 1004px; height: 1200px; overflow: hidden;
    background: var(--page-bg);
  }
  .stage { position: relative; width: 1004px; height: 1200px; }
  .label-margin {
    position: absolute; left: 60px; top: 158px;
    width: 884px; height: 884px; border-radius: 50%;
    background: var(--label-white);
  }
  .label {
    position: absolute; left: 102px; top: 200px;
    width: 800px; height: 800px; border-radius: 50%;
    overflow: hidden; background: var(--label-white);
    border: 3px solid var(--brand-green);
  }
  .label > * { position: absolute; }
  .bands { left: -3px; top: -3px; width: 800px; height: 800px; }
  .brand-name {
    left: 0; width: 800px; top: 105px; text-align: center;
    font: 700 55px/1 "Arvo", serif; color: var(--ink-dark);
    letter-spacing: 1px;
  }
  .brand-tagline {
    right: 252px; top: 173px;
    font: 400 22px/1 "Arvo", serif; color: var(--brand-green);
    letter-spacing: 0.5px;
  }
  .title-top {
    left: 120px; top: 342px;
    font: 600 64px/1 "Montserrat", sans-serif; color: var(--ink-dark);
  }
  .title-main {
    left: 118px; top: 408px;
    font: 600 88px/1 "Montserrat", sans-serif; color: var(--brand-green);
  }
  .rule {
    left: 120px; width: 265px; height: 2px;
    background: linear-gradient(90deg, var(--brand-green) 70%, rgba(60,165,133,0));
  }
  .rule-top { top: 511px; }
  .rule-bottom { top: 571px; }
  .dose {
    left: 120px; top: 523px;
    font: 600 44px/1 "Montserrat", sans-serif; color: var(--ink-dark);
  }
  .dose-label { color: var(--brand-green); }
  .thc-value {
    left: 120px; top: 597px;
    font: 600 30px/1 "Montserrat", sans-serif; color: var(--thc-orange);
  }
  .thc-unit {
    left: 120px; top: 627px;
    font: 600 23px/1 "Montserrat", sans-serif; color: var(--thc-orange);
  }
  .divider { left: 199px; top: 594px; width: 3px; height: 51px; background: var(--ink-dark); }
  .product-name {
    left: 224px; top: 582px;
    font: 300 72px/1 "Roboto Condensed", sans-serif; color: var(--brand-green);
  }
  .product-name sup {
    font: 400 16px/1 "Roboto Condensed", sans-serif; color: var(--brand-green);
    vertical-align: top; margin-left: 4px; position: relative; top: 2px;
  }
  .paw-photo {
    left: 498px; top: 286px; width: 310px; height: 343px;
    background: radial-gradient(ellipse at 60% 45%, var(--fur-light) 0%, #dcd8cf 55%, var(--fur-shade) 80%, rgba(255,255,255,0) 100%);
    border-radius: 40% 0 0 40%;
  }
  .benefits {
    left: 0; width: 800px; top: 700px; text-align: center;
    font: 500 24px/1 "Montserrat", sans-serif; color: var(--label-white);
    display: flex; justify-content: center; align-items: center; gap: 6px;
  }
  .benefits .dot { width: 10px; height: 10px; border-radius: 50%; background: var(--label-white); }
  .net-contents {
    left: 0; width: 800px; top: 742px; text-align: center;
    font: 400 20px/1 "Roboto Condensed", sans-serif; color: var(--label-white);
  }
  .net-contents strong { color: var(--ink-dark); font-weight: 400; }
</style>
</head>
<body>
<main class="stage">
  <div class="label-margin"></div>
  <section class="label">
    <svg class="bands" viewBox="0 0 800 800" aria-hidden="true">
      <path fill="#3ca585" d="M0 195 H800 V235 H356 C322 235 292 252 281 345 C270 252 240 235 190 235 H0 Z"/>
      <rect fill="#3ca585" x="0" y="682" width="800" height="118"/>
    </svg>

    <div class="brand-name">VERDALIS</div>
    <div class="brand-tagline">For Animals</div>

    <div class="paw-photo" role="img" aria-label="Photo of a white dog's front paws resting together"></div>

    <h1 class="title-top">SOOTHING</h1>
    <h2 class="title-main">BALM</h2>
    <div class="rule rule-top"></div>
    <div class="dose"><span class="dose-label">CBD</span> 250MG</div>
    <div class="rule rule-bottom"></div>
    <div class="thc-value">0%</div>
    <div class="thc-unit">THC</div>
    <div class="divider"></div>
    <div class="product-name">Verda Balm<sup>TM</sup></div>

    <div class="benefits">REPAIR <span class="dot"></span> NOURISH <span class="dot"></span> PROTECT</div>
    <div class="net-contents">Net Contents: <strong>40g</strong></div>
  </section>
</main>
</body>
</html>
```